Stationary package for modern new church start
Stationary for Bright Harbor Ministries
Stationary package for modern new church start  - Religion and Spirituality
Creative Brief
Professional
Daniel Mercer
Pastor
Bright Harbor Ministries P.O. Box 67890 Atlanta, GA 30318 The following P.O. Box is a generate one until I obtain one tomorrow. I will provide you with the correct P.O. Box sometime tomorrow or on Friday.
pastormercer@bhmx.org
www.bhmx.org
Please provide me with a complete stationary package that includes: Business Cards Letterhead Pen and pencil Email Signature USB Envelope Folder Fax Option Thank you Card front & Back Compliment Slip CD and CD Cover
Please include the following on the back: The Logo our our Ministry and our email address

```html
<!DOCTYPE html>
<html lang="en">
<head>
<meta charset="utf-8">
<title>Bright Harbor Ministries – Business Card</title>
<link href="https://fonts.googleapis.com/css2?family=Montserrat:wght@400;500;600;700&family=Open+Sans:wght@400;600&display=swap" rel="stylesheet">
<style>
  :root{
    --bg:#e9e7e4;
    --card-white:#ffffff;
    --brand-red:#d8141c;
    --deep-red:#b10c12;
    --accent-blue:#2aa3d8;
    --ink:#4a4a4a;
    --on-red:#ffffff;
  }
  html,body{margin:0;padding:0;width:1200px;height:901px;overflow:hidden;background:var(--bg);}
  .canvas{position:relative;width:1200px;height:901px;}
  .business-card{
    position:absolute;left:130px;top:170px;width:940px;height:560px;
    border-radius:34px;overflow:hidden;background:var(--card-white);
    box-shadow:0 18px 40px rgba(0,0,0,.18);
  }
  .card-shape{position:absolute;inset:0;}
  .brand-block{
    position:absolute;left:40px;top:200px;width:330px;text-align:center;
    font-family:"Montserrat",sans-serif;
  }
  .brand-dot{
    width:90px;height:90px;border-radius:50%;background:var(--brand-red);
    margin:0 auto 22px;
  }
  .brand-name{
    font-weight:700;font-size:29px;line-height:1.15;color:var(--brand-red);margin:0;
  }
  .brand-tagline{
    font-family:"Open Sans",sans-serif;font-size:13px;letter-spacing:1.5px;
    color:var(--ink);margin-top:10px;
  }
  .contact-block{
    position:absolute;left:560px;top:70px;width:330px;color:var(--on-red);
    font-family:"Montserrat",sans-serif;
  }
  .person-name{font-size:25px;font-weight:500;letter-spacing:1px;margin:0;}
  .person-title{font-size:16px;font-weight:400;margin:4px 0 0 2px;}
  .address{font-size:16px;line-height:1.55;margin:42px 0 0 2px;}
  .contact-list{
    list-style:none;margin:0;padding:0;position:absolute;right:46px;top:330px;
    font-family:"Open Sans",sans-serif;font-size:15px;color:var(--on-red);text-align:right;
  }
  .contact-list li{display:flex;align-items:center;justify-content:flex-end;gap:12px;height:33px;}
  .contact-list svg{width:18px;height:18px;flex:none;}
</style>
</head>
<body>
<div class="canvas">
  <div class="business-card">
    <svg class="card-shape" viewBox="0 0 940 560" preserveAspectRatio="none">
      <defs>
        <linearGradient id="redPanel" x1="0" y1="0" x2="1" y2="1">
          <stop offset="0" stop-color="#e8232a"/>
          <stop offset="1" stop-color="#b10c12"/>
        </linearGradient>
      </defs>
      <path d="M440,0 C500,130 360,260 410,400 C432,465 400,520 378,560 L940,560 L940,0 Z" fill="url(#redPanel)"/>
      <path d="M418,0 C478,130 338,260 388,400 C408,462 380,520 358,560" fill="none" stroke="var(--accent-blue)" stroke-width="5"/>
      <path d="M400,0 C458,125 322,250 368,380" fill="none" stroke="var(--accent-blue)" stroke-width="2" opacity=".6"/>
    </svg>

    <div class="brand-block">
      <div class="brand-dot"></div>
      <p class="brand-name">Bright Harbor Ministries</p>
      <div class="brand-tagline">Embodying the Love of Christ</div>
    </div>

    <div class="contact-block">
      <p class="person-name">DANIEL MERCER</p>
      <p class="person-title">Managing Director</p>
      <p class="address">204 9th Floor Plaza<br>Harbor Lane ATL</p>
    </div>

    <ul class="contact-list">
      <li>012 555 0147
        <svg viewBox="0 0 24 24"><path d="M6 2h4l2 5-3 2a12 12 0 0 0 6 6l2-3 5 2v4a2 2 0 0 1-2 2A18 18 0 0 1 4 4a2 2 0 0 1 2-2z" fill="#fff"/></svg></li>
      <li>012 555 0148
        <svg viewBox="0 0 24 24"><rect x="3" y="9" width="18" height="12" rx="2" fill="#fff"/><path d="M4 8c2-4 14-4 16 0" stroke="#fff" stroke-width="3" fill="none"/></svg></li>
      <li>012 555 0149
        <svg viewBox="0 0 24 24"><rect x="6" y="2" width="12" height="20" rx="2" fill="#fff"/><rect x="8" y="5" width="8" height="12" fill="#c4121a"/></svg></li>
      <li>pastormercer@bhmx.org
        <svg viewBox="0 0 24 24"><rect x="2" y="5" width="20" height="14" rx="2" fill="#fff"/><path d="M3 6l9 7 9-7" stroke="#c4121a" stroke-width="2" fill="none"/></svg></li>
      <li>www.bhmx.org
        <svg viewBox="0 0 24 24"><circle cx="12" cy="12" r="9" stroke="#fff" stroke-width="2" fill="none"/><ellipse cx="12" cy="12" rx="4" ry="9" stroke="#fff" stroke-width="2" fill="none"/><path d="M3 12h18" stroke="#fff" stroke-width="2"/></svg></li>
    </ul>
  </div>
</div>
</body>
</html>
```